Mission Statement Board for front lobby

We need a mission statement board for our front lobby at our company called PatternForge. We are a web content management company that builds websites for our clients. We would like two boards, same size, canvas material (not thin poster board or anything like that) size H 3' x L 2', white background, blue and black colored font, our logo on top in blue/gray/black and some blue coloring around top and bottom, kind of framing the white background. Please reference our very rough draft we did in Word so you get an idea of what we're thinking- the attachment shows what we would like on each board. Reference our website to see logo and fonts if you would like, please keep the board similar to our fonts and colors. www.patternforge-example.com

Contact info: Donna Whitlock
Email: donna.whitlock@patternforge-example.com
Phone: 555-217-4039
Updates

Please do not include in a design my contact info, no email donna.whitlock@patternforge-example.com, no phone # 555-217-4039. I added that info to the project when I posted it, but it is not part of the design.... reference attachment posted in project with exactly what we want.

Target Market(s)

Clients & employees in the office who will see the boards in lobby

Industry/Entity Type

It Company

Font styles to use
Other font styles liked:
• reference attachment (but font is flexible within reason)

Colors
33a6d7
0255a3
eaf1f7
0292cd
85cae6
cee9f5
000000
5c5c5c
959595

Requirements
Must have
• Needs to be a professional sign that hangs on wall, company logo, cohesive colors and fonts
Nice to have
• Get creative with the border/framing around the white background
Should not have
• Unprofessional fonts, typos, thin cheap looking poster board materal.

```html
<!DOCTYPE html>
<html lang="en">
<head>
<meta charset="utf-8">
<title>PatternForge Lobby Boards</title>
<link rel="stylesheet" href="https://fonts.googleapis.com/css2?family=Mulish:wght@400;600;800&display=swap">
<style>
  :root {
    --sky: #33a6d7;
    --navy: #0255a3;
    --mist: #eaf1f7;
    --ocean: #0292cd;
    --light-blue: #85cae6;
    --pale-blue: #cee9f5;
    --ink: #000000;
    --charcoal: #5c5c5c;
    --stone: #959595;
    --text: #2b2b2b;
    --backdrop: #4d4c4c;
  }
  * { margin: 0; padding: 0; box-sizing: border-box; }
  html, body { width: 1200px; height: 891px; overflow: hidden; }
  body {
    background: var(--backdrop);
    font-family: "Mulish", Arial, sans-serif;
    position: relative;
  }
  .board {
    position: absolute;
    top: 64px;
    width: 509px;
    height: 764px;
    background: #fff;
    overflow: hidden;
    box-shadow: 0 8px 22px rgba(0,0,0,.45);
  }
  .board--mission { left: 64px; }
  .board--values { left: 630px; }
  .frame-top, .frame-bottom { position: absolute; left: 0; width: 100%; }
  .frame-top { top: 0; height: 240px; }
  .frame-bottom { bottom: 0; height: 120px; }

  .brand {
    position: absolute;
    display: flex;
    align-items: center;
    gap: 10px;
    color: var(--navy);
    font-weight: 800;
  }
  .brand__dot {
    border-radius: 50%;
    background: var(--navy);
    flex: none;
  }
  .board--mission .brand { left: 76px; top: 222px; font-size: 34px; }
  .board--mission .brand__dot { width: 26px; height: 26px; }
  .board--values .brand { left: 70px; top: 180px; font-size: 28px; }
  .board--values .brand__dot { width: 22px; height: 22px; }

  .mission-copy { position: absolute; left: 80px; top: 324px; width: 360px; }
  .mission-copy h2 {
    font-size: 20px; font-weight: 800; color: var(--charcoal); margin-bottom: 10px;
  }
  .mission-copy p {
    font-size: 19px; line-height: 27px; color: var(--text); margin-bottom: 30px;
  }

  .values-title {
    position: absolute; left: 68px; top: 258px;
    font-size: 27px; font-weight: 800; color: var(--charcoal);
    text-shadow: 0 3px 3px rgba(0,0,0,.18);
  }
  .values-list { position: absolute; left: 62px; top: 314px; width: 400px; list-style: none; }
  .value { display: flex; gap: 13px; }
  .value__icon {
    width: 42px; height: 42px; border-radius: 50%; flex: none; margin-top: 5px;
    background: radial-gradient(circle at 35% 30%, var(--ocean), var(--navy) 70%);
    box-shadow: 0 0 0 2px var(--pale-blue);
    display: flex; align-items: center; justify-content: center;
  }
  .value h3 { font-size: 14px; font-weight: 800; color: var(--sky); line-height: 17px; }
  .value p { font-size: 13px; line-height: 17.5px; color: var(--text); }
  .value--integrity { margin-bottom: 19px; }
  .value--accountability { margin-bottom: 19px; }
  .value--respect { margin-bottom: 19px; }
  .value--excellence { margin-bottom: 19px; }

  .site-url {
    position: absolute; right: 36px; bottom: 32px;
    font-size: 13px; color: var(--ocean); letter-spacing: .2px;
  }
  .site-url strong { color: var(--navy); font-weight: 800; }
</style>
</head>
<body>

<section class="board board--mission">
  <svg class="frame-top" viewBox="0 0 509 240" preserveAspectRatio="none" aria-hidden="true">
    <defs>
      <linearGradient id="skyFade" x1="0" y1="0" x2="0" y2="1">
        <stop offset="0" stop-color="#33a6d7"/>
        <stop offset="1" stop-color="#ffffff" stop-opacity="0"/>
      </linearGradient>
    </defs>
    <path d="M0 0H509V170C400 120 300 40 160 60 90 70 40 90 0 110Z" fill="url(#skyFade)" opacity=".75"/>
    <path d="M0 20C140 10 260 60 509 160" stroke="#85cae6" stroke-width="3" fill="none" opacity=".8"/>
    <path d="M0 45C160 30 300 90 509 200" stroke="#cee9f5" stroke-width="6" fill="none" opacity=".9"/>
  </svg>
  <div class="brand"><span class="brand__dot"></span>PatternForge</div>
  <div class="mission-copy">
    <h2>Our Mission Statement</h2>
    <p>We design and implement extraordinary web solutions to help our clients achieve their goals.</p>
    <h2>Our Faith...</h2>
    <p>We reflect the love of Christ in us and through us to our fellow employees, partners and clients.</p>
  </div>
  <svg class="frame-bottom" viewBox="0 0 509 120" preserveAspectRatio="none" aria-hidden="true">
    <defs>
      <linearGradient id="seaFade" x1="0" y1="1" x2="0" y2="0">
        <stop offset="0" stop-color="#33a6d7"/>
        <stop offset="1" stop-color="#ffffff" stop-opacity="0"/>
      </linearGradient>
    </defs>
    <path d="M0 40C120 80 300 70 509 100V120H0Z" fill="url(#seaFade)" opacity=".7"/>
    <path d="M0 70C150 100 330 80 509 110" stroke="#85cae6" stroke-width="3" fill="none"/>
  </svg>
  <div class="site-url">www.<strong>patternforge-example</strong>.com</div>
</section>

<section class="board board--values">
  <svg class="frame-top" viewBox="0 0 509 240" preserveAspectRatio="none" aria-hidden="true">
    <path d="M0 0H509V170C400 120 300 40 160 60 90 70 40 90 0 110Z" fill="url(#skyFade)" opacity=".75"/>
    <path d="M0 20C140 10 260 60 509 160" stroke="#85cae6" stroke-width="3" fill="none" opacity=".8"/>
    <path d="M0 45C160 30 300 90 509 200" stroke="#cee9f5" stroke-width="6" fill="none" opacity=".9"/>
  </svg>
  <div class="brand"><span class="brand__dot"></span>PatternForge</div>
  <h2 class="values-title">Our Core Values</h2>
  <ul class="values-list">
    <li class="value value--integrity">
      <span class="value__icon"></span>
      <div><h3>Integrity</h3><p>We believe that to be successful, it is essential to operate at the highest levels of honesty, responsibility and trust.</p></div>
    </li>
    <li class="value value--accountability">
      <span class="value__icon"></span>
      <div><h3>Accountability</h3><p>Taking responsibility for one’s own actions.</p></div>
    </li>
    <li class="value value--respect">
      <span class="value__icon"></span>
      <div><h3>Respect</h3><p>Understand and value differences in others. Listen thoughtfully to understand.</p></div>
    </li>
    <li class="value value--excellence">
      <span class="value__icon">
        <svg width="18" height="18" viewBox="0 0 18 18" aria-hidden="true"><path d="M3 9.5l4 4 8-9" stroke="#fff" stroke-width="2.4" fill="none" stroke-linecap="round"/></svg>
      </span>
      <div><h3>Excellence</h3><p>We continually improve our standards and processes so that excellence simple becomes a natural consequence of our work.</p></div>
    </li>
    <li class="value value--loyalty">
      <span class="value__icon"></span>
      <div><h3>Loyalty</h3><p>Working collaboratively with PatternForge employees, partners and customers to solve problems and achieve goals.</p></div>
    </li>
  </ul>
  <svg class="frame-bottom" viewBox="0 0 509 120" preserveAspectRatio="none" aria-hidden="true">
    <path d="M0 40C120 80 300 70 509 100V120H0Z" fill="url(#seaFade)" opacity=".7"/>
    <path d="M0 70C150 100 330 80 509 110" stroke="#85cae6" stroke-width="3" fill="none"/>
  </svg>
  <div class="site-url">www.<strong>patternforge-example</strong>.com</div>
</section>

</body>
</html>
```